Business Card Design Project

I would like a business card created for a new company. This is a holding company that acts as my investment company. It holds real estate and service based companies. The name of the company is Sandorecca which is Italian for Evolution. Defined as development or growth.
We currently have no logo. I really like some of the "different" cards out there. Potentially metallic or grey/black. That looks premium/hi-end and unique. I am not sure if your design would be specific to the card stock I end with our just logo/design/font.
Real Estate

```html
<!DOCTYPE html>
<html lang="en">
<head>
<meta charset="utf-8">
<title>Sandorecca Stationery</title>
<link href="https://fonts.googleapis.com/css2?family=Arimo:wght@400;700&display=swap" rel="stylesheet">
<style>
  :root {
    --ink: #141414;
    --ink-soft: #1e1e1e;
    --blue: #1d8fd6;
    --paper: #eef0f6;
    --paper-edge: #dfe2ea;
    --text: #2a2a2a;
    --muted: #cfd3da;
    --stage: #d9dbdf;
  }
  * { margin: 0; padding: 0; box-sizing: border-box; }
  html, body { width: 1200px; height: 900px; overflow: hidden; }
  body { background: var(--stage); font-family: "Arimo", Arial, sans-serif; color: var(--text); position: relative; }

  .sheet { position: absolute; background: var(--paper); box-shadow: 0 6px 18px rgba(0,0,0,.25); overflow: hidden; }

  .brand-band { background: var(--ink); position: relative; }
  .wordmark { font-family: "Arimo", Arial, sans-serif; font-weight: 700; color: var(--blue); text-transform: uppercase; letter-spacing: .12em; display: flex; align-items: center; gap: 8px; }
  .wordmark .mark-dot { width: 10px; height: 10px; background: var(--blue); display: inline-block; }
  .contact { color: #f2f2f2; font-size: 8px; line-height: 1.4; }
  .contact .label { color: var(--blue); }

  .accent-rule { display: flex; height: 8px; border-top: 3px solid var(--ink); }
  .accent-rule .blue { background: var(--blue); }
  .accent-rule .light { background: var(--paper); flex: 1; }

  /* Letterhead */
  .letterhead { left: 40px; top: 40px; width: 470px; height: 630px; }
  .letterhead .brand-band { height: 108px; padding: 40px 0 0 36px; }
  .letterhead .wordmark { font-size: 26px; }
  .letterhead .contact { position: absolute; right: 26px; top: 16px; }
  .letterhead .accent-rule .blue { width: 72%; }
  .letter-body { padding: 26px 44px 0 44px; font-size: 9.5px; line-height: 1.35; }
  .letter-body p { margin-bottom: 11px; text-align: justify; }
  .closing { margin-top: 4px; }
  .signature-area { width: 150px; height: 42px; background: #e2e5ec; margin: 8px 0 4px; }
  .signer { font-size: 9.5px; margin-left: 110px; margin-top: -22px; line-height: 1.3; }
  .letter-url { position: absolute; left: 44px; bottom: 26px; font-size: 13px; letter-spacing: .45em; color: var(--ink); }
  .letter-foot { position: absolute; left: 0; right: 0; bottom: 0; height: 9px; display: flex; }
  .letter-foot .blue { width: 74%; background: var(--blue); }
  .letter-foot .dark { flex: 1; background: var(--ink); }

  /* Envelope */
  .envelope { left: 540px; top: 40px; width: 620px; height: 290px; }
  .envelope .brand-band { height: 112px; padding: 46px 0 0 36px; }
  .envelope .wordmark { font-size: 28px; }
  .envelope .contact { position: absolute; right: 26px; top: 18px; }
  .envelope .accent-rule .blue { width: 70%; }
  .envelope-foot { position: absolute; left: 0; bottom: 0; height: 7px; width: 68%; background: var(--blue); }

  /* Business cards */
  .card { top: 380px; width: 300px; height: 172px; background: var(--ink); }
  .card-front { left: 540px; }
  .card-back { left: 860px; }
  .card-stripe { position: absolute; left: 0; right: 0; bottom: 0; height: 10px; display: flex; }
  .card-stripe .blue { width: 70%; background: var(--blue); }
  .card-stripe .light { flex: 1; background: var(--paper); }

  .card-front .wordmark { position: absolute; left: 0; right: 0; top: 58px; justify-content: center; font-size: 24px; }
  .card-front .card-url { position: absolute; left: 0; right: 0; top: 96px; text-align: center; color: #d8d8d8; font-size: 7.5px; letter-spacing: .55em; }

  .card-back .wordmark { position: absolute; left: 0; right: 0; top: 30px; justify-content: center; font-size: 21px; }
  .card-back .details { position: absolute; left: 0; right: 0; top: 68px; text-align: center; color: #e6e6e6; font-size: 7px; line-height: 1.45; }
  .card-back .person { color: var(--blue); font-weight: 700; font-size: 9px; letter-spacing: .04em; }
  .card-back .role { font-size: 6.5px; margin-bottom: 3px; }
  .card-back .web { color: var(--blue); font-size: 9.5px; margin-top: 2px; }
</style>
</head>
<body>

  <section class="sheet letterhead">
    <header class="brand-band">
      <div class="wordmark"><span class="mark-dot"></span>Sandorecca</div>
      <address class="contact">
        2400 Alder Ave. #5,<br>Pasadena, CA 91101<br><br>
        <span class="label">cell:</span> +1 555.210.4400<br>
        <span class="label">office:</span> +1 555.318.0000 x1204<br>
        <span class="label">phone:</span> +1 (555) 427-9031<br>
        <span class="label">email:</span> marco@sandorecca.com
      </address>
    </header>
    <div class="accent-rule"><span class="blue"></span><span class="light"></span></div>
    <div class="letter-body">
      <p>Dear Client,</p>
      <p>Lorem ipsum dolor sit amet, consectetur adipisicing elit, sed do eiusmod tempor incididunt ut labore et dolore magna aliqua. Ut enim ad minim veniam, quis nostrud exercitation ullamco laboris nisi ut aliquip ex ea commodo consequat. Duis aute irure dolor in reprehenderit in voluptate velit esse cillum dolore eu fugiat nulla pariatur. Excepteur sint occaecat cupidatat non proident, sunt in culpa qui officia deserunt mollit anim id est laborum.</p>
      <p>Lorem ipsum dolor sit amet, consectetur adipisicing elit, sed do eiusmod tempor incididunt ut labore et dolore magna aliqua. Ut enim ad minim veniam, quis nostrud exercitation ullamco laboris nisi ut aliquip ex ea commodo consequat. Duis aute irure dolor in reprehenderit in voluptate velit esse cillum dolore eu fugiat nulla pariatur. Excepteur sint occaecat cupidatat non proident, sunt in culpa qui officia deserunt mollit anim id est laborum.</p>
      <p>Lorem ipsum dolor sit amet, consectetur adipisicing elit, sed do eiusmod tempor incididunt ut labore et dolore magna aliqua. Ut enim ad minim veniam, quis nostrud exercitation ullamco laboris nisi ut aliquip ex ea commodo consequat. Duis aute irure dolor in reprehenderit in voluptate velit esse cillum dolore eu fugiat nulla pariatur. Excepteur sint occaecat cupidatat non proident, sunt in culpa qui officia deserunt mollit anim id est laborum.</p>
      <p>Lorem ipsum dolor sit amet, consectetur adipisicing elit, sed do eiusmod tempor incididunt ut labore et dolore magna aliqua. Ut enim ad minim veniam, quis nostrud exercitation ullamco laboris nisi ut aliquip ex ea commodo consequat. Duis aute irure dolor in reprehenderit in voluptate velit esse cillum dolore eu fugiat nulla pariatur. Excepteur sint occaecat cupidatat non proident, sunt in culpa qui officia deserunt mollit anim id est laborum.</p>
      <p class="closing">Yours Sincerely,</p>
      <div class="signature-area" role="img" aria-label="Handwritten signature of the sender"></div>
      <p class="signer">Elena Rossi<br>Executive manager</p>
    </div>
    <div class="letter-url">www.sandorecca.com</div>
    <div class="letter-foot"><span class="blue"></span><span class="dark"></span></div>
  </section>

  <section class="sheet envelope">
    <header class="brand-band">
      <div class="wordmark"><span class="mark-dot"></span>Sandorecca</div>
      <address class="contact">
        2400 Alder Ave. #5, Pasadena, CA 91101<br><br>
        <span class="label">cell:</span> +1 555.210.4400<br>
        <span class="label">office:</span> +1 555.318.0000 x1204<br>
        <span class="label">phone:</span> +1 (555) 427-9031<br>
        <span class="label">email:</span> marco@sandorecca.com
      </address>
    </header>
    <div class="accent-rule"><span class="blue"></span><span class="light"></span></div>
    <div class="envelope-foot"></div>
  </section>

  <section class="sheet card card-front">
    <div class="wordmark"><span class="mark-dot"></span>Sandorecca</div>
    <div class="card-url">www.sandorecca.com</div>
    <div class="card-stripe"><span class="blue"></span><span class="light"></span></div>
  </section>

  <section class="sheet card card-back">
    <div class="wordmark"><span class="mark-dot"></span>Sandorecca</div>
    <div class="details">
      <div class="person">MARCO BELLANDI</div>
      <div class="role">Owner</div>
      2400 Alder Ave. #5, Pasadena, CA 91101<br>
      c: +1 555.210.4400 &nbsp; o: +1 555.318.0000 x1204<br>
      p: +1 (555) 427-9031 &nbsp; e: marco@sandorecca.com
      <div class="web">www.sandorecca.com</div>
    </div>
    <div class="card-stripe"><span class="blue"></span><span class="light"></span></div>
  </section>

</body>
</html>
```